Jewelry Manufacturing & Repair business needs advertising mailout - 9x4 flyer

Need new double sided flyer designed for an insert into a mailout. Want 9x4 (vertical design) to fit in 9.5" x 4.125" envelopes. Company based out of Louisiana called "Lem Travis Manufacturing." Been in business for 45 years. We specialize in custom jewelry design and casting on the wholesale level. We are a full service trade shop offering CAD design, casting services, basic and advanced jewelry repair. Most of our customers are drawn to the fact that they talk directly with the owner/designer of the company each time they call. I've attached several images of CAD renders we've built and of our logo. I've also attached a copy of an old mailout we sent out 10 years ago that I designed myself (and it needed a lot of work). The business information listed in this old mailout is correct, except that we’ve been in business 45 years now. I would like the final design to be "business bold," portraying business strength and stability. I like shades of blue, or a gold/silver color scheme. Logo is black and white. Need double sided.

Looking for project to be less wordy than the 10 yr old mailout. Lem’t need the “example scenario” in this flyer.
Updates

The weekend has made the 2 day timeframe very tight. Would like to extend timeframe, but I will select a design on Monday at 3:00 pm (USA Central time).

Target Market(s)

Retail Jewelry Stores

Industry/Entity Type

Jewelry

Colors
cfdeed
0455a3
3176b5
85acd3

Requirements
Must have
• All contact information.
Nice to have
• Purpose of this flyer is to get new accounts for our business. We want something that the retail jewelry store will notice something that will make them not throw away immediately, but instead hold onto for the future.
• This upcoming Christmas season is usually very busy for retail stores, so we can help take some of the overflow of work and still meet deadlines. With our help, they shouldn't have to turn any customer away.
Should not have
• We will be partnering in this mailout with a sister wholesale diamond company. Therefore, we don't want to mention that our company sells any diamonds, as we want to leave that part up to our sister company.

```html
<!DOCTYPE html>
<html lang="en">
<head>
<meta charset="utf-8">
<title>Lem Travis Manufacturing – Mailout Flyer</title>
<link href="https://fonts.googleapis.com/css2?family=Arvo&family=Encode+Sans+Semi+Condensed:wght@300;400;600&family=Signika:wght@300;400;600;700&display=swap" rel="stylesheet">
<style>
:root{
  --bg:#e2e2e2;
  --paper:#fefdf9;
  --cream:#f4ecd2;
  --gold:#e3b51f;
  --gold-soft:#e8d9a6;
  --ink:#111;
  --rule:#c9c9c9;
}
*{margin:0;padding:0;box-sizing:border-box}
html,body{width:1200px;height:1084px;overflow:hidden;background:var(--bg)}
body{position:relative;font-family:"Encode Sans Semi Condensed",sans-serif;font-weight:300;color:var(--ink)}
.panel{position:absolute;background:var(--paper);box-shadow:0 8px 14px rgba(0,0,0,.12);overflow:hidden}
.panel--front{left:194px;top:116px;width:358px;height:799px}
.panel--back{left:657px;top:115px;width:354px;height:800px}
.texture{position:absolute;inset:0;background:linear-gradient(180deg,#fffefb 0%,#fbf8ee 100%)}
.hero{position:absolute;left:0;top:0;width:358px;height:175px;background:linear-gradient(180deg,#8d8d8d 0%,#c9c9c9 60%,#f4f4f2 100%)}
.hero-ring{position:absolute;left:205px;top:55px;width:70px;height:80px;border-radius:40%;background:radial-gradient(circle,#e5c04a 0%,#b48a1e 60%,transparent 72%)}
.brand-box{position:absolute;left:30px;top:46px;width:137px;height:96px;border:2px solid #fff;display:flex;align-items:center;justify-content:center;text-align:center;font-family:"Arvo",serif;font-size:19px;line-height:1.15;color:#fff}
.banner{position:absolute;left:30px;top:169px;width:299px;height:35px;background:var(--gold);font-family:"Arvo",serif;font-size:17px;display:flex;align-items:center;justify-content:center;white-space:nowrap}
.banner::before{content:"";position:absolute;left:212px;top:-9px;border:9px solid transparent;border-top:0;border-bottom-color:var(--gold)}
.tagline{position:absolute;left:30px;top:206px;width:299px;font-family:"Signika",sans-serif;font-size:8px;font-weight:400;border-bottom:1px solid #555;padding-bottom:2px;white-space:nowrap}
.tagline em{font-style:italic}
.headline{position:absolute;font-family:"Signika",sans-serif;font-weight:300;font-size:20px;line-height:1.05;color:var(--ink);white-space:nowrap}
.headline b{font-weight:600;color:var(--gold)}
.body{position:absolute;font-size:11.5px;line-height:1.15;text-align:justify;color:var(--ink)}
.body p+p{margin-top:12px}
.body .drop{font-size:17px;font-weight:400;line-height:0}
.body strong{font-weight:600}
.offer{position:absolute;left:90px;top:623px;font-size:11.5px;line-height:1.2;list-style:none}
.offer li{position:relative;padding-left:14px}
.offer li::before{content:"";position:absolute;left:0;top:7px;width:3px;height:3px;background:var(--ink)}
.footer-glow{position:absolute;left:0;right:0;bottom:0;height:110px;background:linear-gradient(180deg,rgba(244,236,210,0) 0%,var(--cream) 70%)}
.footer-art{position:absolute;bottom:0;height:72px;border-radius:40% 40% 0 0;background:radial-gradient(ellipse at center,#efe2b8 0%,rgba(239,226,184,0) 70%)}
.footer-rule{position:absolute;left:0;right:0;top:750px;height:1px;background:var(--gold-soft)}
.phone-badge{position:absolute;top:737px;width:156px;height:28px;background:#111;border:1px solid var(--gold);border-radius:5px;color:var(--gold);font-family:"Signika",sans-serif;font-weight:700;font-size:19px;display:flex;align-items:center;justify-content:center}
.phone-badge::before{content:"";position:absolute;left:10px;top:-7px;border:6px solid transparent;border-top:0;border-bottom-color:#111}
.call{position:absolute;left:74px;top:551px;font-family:"Signika",sans-serif;font-weight:300;font-size:16px;line-height:1.15}
.call b{font-weight:700}
.call-rule{position:absolute;height:1px;background:var(--gold-soft)}
.company{position:absolute;left:78px;top:597px;font-family:"Arvo",serif;font-size:16px;line-height:1}
.address{position:absolute;left:78px;top:639px;display:flex;gap:5px;font-family:"Signika",sans-serif;font-weight:300;font-size:14px;line-height:1.1}
.address small{font-size:11px}
.contacts{position:absolute;left:78px;top:682px;font-family:"Signika",sans-serif;font-weight:300;font-size:14px;line-height:1.05;border-collapse:collapse}
.contacts td{padding:0}
.contacts td:first-child{width:58px}
.contacts .small{font-size:11px}
</style>
</head>
<body>

<section class="panel panel--front" aria-label="Flyer front">
  <div class="texture"></div>
  <div class="hero" role="img" aria-label="Black and white photo of a jeweler's hand holding a gold ring"><div class="hero-ring"></div></div>
  <div class="brand-box">Lem Travis<br>Mfg</div>
  <div class="banner">Lem Travis Manufacturing, LLC</div>
  <div class="tagline">TOP QUALITY CRAFTSMANSHIP, FRIENDLY PERSONAL SERVICE, <em>EST. 1974</em></div>

  <h1 class="headline" style="left:52px;top:237px">Are you <b>looking</b> for a way to<br>increase <b>profits</b>?</h1>
  <div class="body" style="left:81px;top:290px;width:220px">
    <p><span class="drop">M</span>any shoppers choose a new jewelry store because they need a repair. Offering a full range of services keeps those customers coming back.</p>
    <p><strong>Lem Travis Manufacturing</strong> is the skilled trade shop behind your counter. You talk directly with the owner and designer every time you call.</p>
  </div>

  <h2 class="headline" style="left:52px;top:475px">Who <b>We Are:</b></h2>
  <div class="body" style="left:81px;top:504px;width:220px">
    <p><span class="drop">W</span>e are a family operated business, serving the jewelry industry for over 45 years, with quality craftsmanship and fast, honest, courteous service.</p>
  </div>

  <h2 class="headline" style="left:52px;top:599px">What <b>We Offer:</b></h2>
  <ul class="offer">
    <li>Basic &amp; advanced jewelry repair</li>
    <li>Custom hand carved wax modeling</li>
    <li>CAD / CAM services for intricate detail</li>
    <li>Gold &amp; Platinum casting</li>
    <li>Furnish waxes, raw castings or finished<br>products</li>
  </ul>

  <div class="footer-glow"></div>
  <div class="footer-art" style="left:40px;width:110px" role="img" aria-label="Faded photo of gold rings"></div>
  <div class="footer-art" style="left:160px;width:90px" role="img" aria-label="Faded photo of a gold ring"></div>
  <div class="footer-rule"></div>
  <div class="phone-badge" style="left:79px">1-888-555-0142</div>
</section>

<section class="panel panel--back" aria-label="Flyer back">
  <div class="texture"></div>
  <h2 class="headline" style="left:49px;top:32px">How <b>It Works:</b></h2>
  <div class="body" style="left:78px;top:62px;width:219px">
    <p><span class="drop">S</span>hip your jewelry to us safely through a major carrier (ParcelWing, SwiftShip, Courier One). With insured overnight delivery, your work is back within a couple days.</p>
    <p>From a simple sketch, we create custom pieces in yellow gold, white gold, or platinum, by hand carved wax or CAD/CAM, then cast and finish them.</p>
    <p>We also carve and cast wedding bands, pendants, earrings and more. If you can dream it, we can create it.</p>
    <p><strong>Busy holiday season?</strong> Send us your overflow. We help you meet every deadline, so you never have to turn a customer away.</p>
  </div>

  <div class="call-rule" style="left:0;width:66px;top:560px"></div>
  <div class="call">CALL <b>LEM</b> OR<br><b>GRANT TRAVIS</b></div>
  <div class="call-rule" style="left:222px;right:0;top:582px"></div>

  <div class="company">Lem Travis<br>Manufacturing, LLC</div>
  <div class="address">
    <svg width="14" height="20" viewBox="0 0 14 20" aria-hidden="true"><path d="M7 0C3.1 0 0 3.1 0 7c0 5 7 13 7 13s7-8 7-13c0-3.9-3.1-7-7-7z" fill="#111"/><circle cx="7" cy="7" r="3" fill="#fff"/></svg>
    <div><small>12</small> Heron Lane<br>Marsh Bend, LA &nbsp;<small>71200</small></div>
  </div>
  <table class="contacts">
    <tr><td>Phone</td><td class="small">: 1-888-555-0142</td></tr>
    <tr><td>Local</td><td class="small">: 318-555-0176</td></tr>
    <tr><td>E-mail</td><td>: grant@ltravismfg.com</td></tr>
  </table>

  <div class="footer-glow"></div>
  <div class="footer-art" style="left:90px;width:90px" role="img" aria-label="Faded photo of a gold ring"></div>
  <div class="footer-art" style="left:200px;width:110px" role="img" aria-label="Faded photo of a cluster ring"></div>
  <div class="footer-rule"></div>
  <div class="phone-badge" style="left:63px">1-888-555-0142</div>
</section>

</body>
</html>
```